Brackenmoor Heating Supplies Ltd Needs a 2 sided A5 Flyer Design

We need a flyer design for our company to promote Air and ground Source Heat Pumps in the Devon and Cornwall region of the UK.

Our Government has launched the RHI (renewable heat incentive) a 7 year quarterly payment to offset the cost of installation..
Homeowners currently using OIL or LPG gas for there heating and hot water will save up to 50% on there energy bill by swapping to a heat pump,
Currently education is needed to the potential end user on the benefits of heat pumps,
This flyer will be part of an initial start point to get the homeowner to book a free survey to discuss there options, We are a renewable energy company with great local knowledge, and a wealth of experience ......

KEY points SAVINGS OF UP TO 50% on OIL or LPG heating and hot water systems

RHI PAYMENTS FROM GOVERNMENT FOR 7 years

HONEST IMPARTIAL ADVICE ON SOLUTIONS

FREE SURVEYS ON ALL RENEWABLE SOLUTIONS AND COSTINGS. website www.brackenmoorheat.co.uk have included some potential wording

LOGOS FROM SUPPLIERS

We think side one should be high impact on high oil and LPG gas costs, harm to environment and potential 50% savings with a heat pump. Side 2 to be RHI 7 year quarterly payment and a little about our company offering expertise and free impartial advice and survey

general theme a "striking call to action"

Target Market(s)

Target market is 40 to 60 year old home owners that are off gas grid and use oil or LPG for heating and hot water

Industry/Entity Type

Environment

Font styles to use
Serif
Sans Serif

Colors
33a6d7
f04a50
00a88f
fbed22

Requirements
Must have
• savings 50% on oil or LPG energy costs for heating and hot water

RHI (renewable heat incentive) government backed payments to offset cost of instalation

7 year payments averaging £1000 a year

FREE impartial advice and surveys

```html
<!DOCTYPE html>
<html lang="en">
<head>
<meta charset="utf-8">
<title>Air and Ground Source Heat Pumps – Brackenmoor Heating Supplies</title>
<link rel="stylesheet" href="https://fonts.googleapis.com/css2?family=Montserrat:wght@800&family=Lato:ital,wght@0,400;0,700;0,900;1,900&family=Roboto+Condensed:wght@700&display=swap">
<style>
  :root{
    --green:#66b245;
    --green-dark:#2f7d3a;
    --green-text:#3d9a3a;
    --green-light:#9fd37a;
    --white:#ffffff;
  }
  *{margin:0;padding:0;box-sizing:border-box}
  html,body{width:846px;height:1200px;overflow:hidden;background:var(--white)}
  .flyer{position:relative;width:846px;height:1200px;background:var(--green);font-family:"Lato",sans-serif;color:var(--white);overflow:hidden}
  .hero{position:absolute;left:0;top:0;width:846px;height:400px;background:var(--white)}
  .hero-hills{position:absolute;left:0;top:0}
  .skyline{position:absolute;left:430px;top:30px;width:416px;height:255px;background:linear-gradient(180deg,#a8d98a 0%,#6cbf4a 100%);border-radius:0 0 0 40px}
  .headline{position:absolute;left:53px;top:44px;font-family:"Montserrat",sans-serif;font-weight:800;font-size:54px;line-height:66px;color:var(--green-text);letter-spacing:0.5px}
  .rhi-title{position:absolute;left:52px;top:400px;font-size:42px;font-weight:400;letter-spacing:0.5px;line-height:48px}
  .rhi-sub{position:absolute;left:52px;top:446px;font-size:22px;line-height:24px}
  .rhi-amount{position:absolute;left:56px;top:487px;font-size:20px;line-height:26px}
  .rhi-amount strong{font-weight:900;font-size:23px}
  .fuel-band{position:absolute;left:0;top:528px;width:846px;height:56px;background:var(--white);display:flex;align-items:center;padding-left:48px}
  .fuel-band p{font-family:"Roboto Condensed",sans-serif;font-weight:700;font-size:27px;color:var(--green-dark)}
  .fit-band{position:absolute;left:0;top:598px;width:846px;height:98px;background:var(--white)}
  .fit-band p{position:absolute;left:52px;top:8px;width:580px;font-size:18.5px;line-height:24px;color:var(--green-dark)}
  .system-diagram{position:absolute;left:672px;top:2px;width:146px;height:90px;background:linear-gradient(180deg,#eef1f3,#cfd6dc)}
  .benefits{position:absolute;left:38px;top:707px;width:760px;list-style:none}
  .benefits li{position:relative;padding-left:16px;font-size:19px;line-height:24px;margin-bottom:24px}
  .benefits li::before{content:"";position:absolute;left:0;top:9px;width:8px;height:8px;border-radius:50%;background:var(--white)}
  .maintenance{position:absolute;left:46px;top:838px;width:751px;height:54px;background:var(--white);border-radius:8px;display:flex;align-items:center;justify-content:center;text-align:center;padding:0 10px}
  .maintenance p{font-style:italic;font-weight:900;font-size:14.2px;line-height:19px;color:var(--green-text)}
  .about{position:absolute;left:53px;top:904px;width:750px}
  .about p{font-size:9.4px;font-weight:700;line-height:12.5px;margin-bottom:11.5px}
  .call{position:absolute;left:40px;top:1071px;width:766px;text-align:center;font-size:15.5px;font-weight:700;line-height:20px}
  .contact-band{position:absolute;left:0;top:1120px;width:846px;height:52px;background:var(--white);display:flex;align-items:center}
  .contact{display:flex;align-items:center;font-family:"Lato",sans-serif;font-weight:900;font-size:28px;color:var(--green-text);letter-spacing:0.5px}
  .contact svg{margin-right:14px}
  .contact.phone{margin-left:100px}
  .contact.web{margin-left:95px}
</style>
</head>
<body>
<div class="flyer">
  <div class="hero">
    <div class="skyline" role="img" aria-label="Illustration of a green city skyline with trees, houses, a wind turbine and birds"></div>
    <svg class="hero-hills" width="846" height="400" viewBox="0 0 846 400" aria-hidden="true">
      <path d="M0 360 C200 330 420 300 600 270 C720 250 800 245 846 240 L846 400 L0 400 Z" fill="#8cc862"/>
      <path d="M0 372 C240 345 470 320 640 300 C740 288 810 282 846 280 L846 400 L0 400 Z" fill="#6ab548"/>
      <path d="M560 310 C680 285 780 272 846 262 L846 360 C760 340 660 325 560 310 Z" fill="#2f8a3e" opacity="0.55"/>
    </svg>
    <h1 class="headline">AIR and GROUND<br>SOURCE HEAT<br>PUMPS</h1>
  </div>

  <h2 class="rhi-title">GOVERNMENT BACKED RHI</h2>
  <p class="rhi-sub">(RENEWABLE HEAT INCENTIVE )</p>
  <p class="rhi-amount"><strong>£1,000</strong> A YEAR PAYMENTS ON AVERAGE FOR 7 YEARS FOR INSTALATION</p>

  <div class="fuel-band"><p>You will no longer have to pay for high priced Oil and LPG.</p></div>

  <div class="fit-band">
    <p>Air source heat pumps will fit into your current radiator heating system in most cases, and will provide all of your heating and hot water needs for the home.</p>
    <div class="system-diagram" role="img" aria-label="Cutaway drawing of a house showing a heat pump connected to radiators and a hot water cylinder"></div>
  </div>

  <ul class="benefits">
    <li>RHI payments are paid by the Government for 7 years every quarter directly into your bank&nbsp; to offset the initial cost of equipment.</li>
    <li>Ongoing savings year on year of 50% compared to your current fuel usage. Saving between £500 and £1200.</li>
  </ul>

  <div class="maintenance"><p>Heat pumps require little maintenance and have a life expectancy of 25+ years; where after just the main unit would have to be replaced, making replacement expectation similar to a standard boiler.</p></div>

  <div class="about">
    <p>In October of 2014 the Government finalised the groundbreaking RHI renewable heat incentive. We are the first country in the world to give payments to cover the install cost of renewable technology based around heating and hot water.</p>
    <p>At Brackenmoor Heating Supplies we are in a unique position to advise you on the options open to you to replace your Oil and LPG boilers in favour of products that are 50% cheaper to run and are also kinder to the environment.</p>
    <p>We have 15 years experience in the Renewable Energy market and are not tied to one supplier or one technology. This puts us in a position to discuss ALL the options that are open to you to enable you to make a correct informed decision.</p>
    <p>We are able to manage your project from start to finish and ongoing servicing; with a staff of 20 we do not sub our work to other contractors allowing us to give the end user confidence and peace of mind before, during and after install.</p>
    <p>Please get in touch and we are happy to give free impartial advice on options open to you.</p>
  </div>

  <p class="call">Call our Plymouth based office and asks to speak to Daniel our Energy Consultant or Owen Hartley our Technical Director and they will be pleased to inform you further.</p>

  <div class="contact-band">
    <div class="contact phone">
      <svg width="30" height="30" viewBox="0 0 30 30" aria-hidden="true"><rect width="30" height="30" rx="6" fill="#555"/><path d="M10 7c1.2-.6 2 .2 2.6 1.5l1 2.2c.4 1-.2 1.6-1 2.1-.5.3-.5.8-.2 1.4 1 1.8 2 3 3.5 4 .5.3 1 .3 1.4-.2.6-.8 1.2-1.3 2.2-.8l2 1.1c1.2.7 1.5 1.6.7 2.7-1.2 1.6-3 2-5 1C13 20.600 9.600 17 8 12.500 7.300 10 8 8 10 7z" fill="#fff"/></svg>
      <span>0175289430</span>
    </div>
    <div class="contact web">
      <svg width="30" height="30" viewBox="0 0 30 30" aria-hidden="true"><rect width="30" height="30" rx="6" fill="#e8e8e8"/><path d="M15 6 5 15h3v9h5v-6h4v6h5v-9h3z" fill="#333"/></svg>
      <span>www.brackenmoorheat.co.uk</span>
    </div>
  </div>
</div>
</body>
</html>
```